Advert for Services that we offer

Bolt Remova Ltd need an design to represent what we do in a modern way by showing an image with a brief description and the use of corporate logo the information we will proved vie a doc file and this is to be presented in a modern way. This design will be for print & web. we have done our own design and its not great i have put this in the file repository

Target Market(s)

Motor trade

Font styles to use
Sans Serif

Colors

Designer to choose colors to be used in the design.

Requirements
Must have
• Company colour scheme as per logo within the files uploaded.
• and a small boarder to isolate it from the rest of the articles.
Nice to have
• Modern font
Should not have
• Old style font

```html
<!DOCTYPE html>
<html lang="en">
<head>
<meta charset="utf-8">
<title>Bolt Remova Ltd – Product Testing &amp; Analysis</title>
<link rel="stylesheet" href="https://fonts.googleapis.com/css2?family=Montserrat:wght@300;500;600;700&display=swap">
<style>
  :root {
    --page-bg: #e9edf2;
    --brand-blue: #1f6db5;
    --brand-blue-deep: #155a9c;
    --accent-grey: #a3a7ad;
    --band-dark: #1b1b1d;
    --text-light: #ffffff;
    --text-soft: #e6eef7;
    --logo-blue: #2b82d0;
  }
  * { margin: 0; padding: 0; box-sizing: border-box; }
  html, body {
    width: 1200px; height: 920px; overflow: hidden;
    background: var(--page-bg);
    font-family: "Montserrat", Arial, sans-serif;
  }
  .advert-frame {
    position: absolute; left: 50px; top: 101px;
    width: 1100px; height: 718px; overflow: hidden;
  }
  .advert {
    position: absolute; left: 0; top: 0;
    width: 820px; height: 535px;
    transform: scale(1.3415); transform-origin: 0 0;
  }
  .advert-shapes { position: absolute; inset: 0; }
  .advert-copy { position: absolute; left: 48px; top: 52px; color: var(--text-light); }
  .headline-light { font-weight: 300; font-size: 30px; line-height: 34px; letter-spacing: 0.3px; }
  .headline-bold { font-weight: 700; font-size: 31px; line-height: 38px; letter-spacing: 0.2px; }
  .divider { width: 24px; height: 2px; background: var(--text-light); margin: 14px 0 22px; }
  .service-list { list-style: none; }
  .service-item {
    display: flex; align-items: center; height: 43px;
    font-weight: 500; font-size: 22.5px; color: var(--text-soft);
  }
  .service-number {
    width: 26px; height: 26px; border-radius: 50%;
    background: var(--text-light); color: var(--brand-blue);
    font-weight: 700; font-size: 17px;
    display: flex; align-items: center; justify-content: center;
    margin-right: 14px; margin-left: -4px;
  }
  .divider-lower { margin: 18px 0 20px; }
  .contact-phone, .contact-web { font-weight: 700; font-size: 26px; line-height: 31px; }
  .company-name {
    position: absolute; left: 460px; top: 452px; width: 330px;
    text-align: center; color: var(--logo-blue);
    font-weight: 600; font-size: 21px; letter-spacing: 1px;
  }
</style>
</head>
<body>
  <div class="advert-frame">
    <div class="advert">
      <svg class="advert-shapes" viewBox="0 0 820 535" width="820" height="535">
        <defs>
          <linearGradient id="photo-tone" x1="0" y1="0" x2="1" y2="0">
            <stop offset="0" stop-color="#dfe2e6"/>
            <stop offset="0.45" stop-color="#b9bdc2"/>
            <stop offset="0.7" stop-color="#3d424a"/>
            <stop offset="1" stop-color="#2a2e34"/>
          </linearGradient>
          <linearGradient id="panel-blue" x1="0" y1="0" x2="0" y2="1">
            <stop offset="0" stop-color="var(--brand-blue)"/>
            <stop offset="1" stop-color="var(--brand-blue-deep)"/>
          </linearGradient>
        </defs>
        <rect class="photo-area" x="380" y="0" width="440" height="398" fill="url(#photo-tone)"
              role="img" aria-label="Photo of a technician in safety glasses measuring a flanged bore with a digital gauge"/>
        <rect class="logo-band" x="360" y="398" width="460" height="137" fill="var(--band-dark)"/>
        <path class="accent-curve" d="M0 0 H434 C484 80 514 200 494 290 C479 380 434 470 389 535 H0 Z" fill="var(--accent-grey)"/>
        <path class="blue-panel" d="M0 0 H420 C470 80 500 200 480 290 C465 380 420 470 375 535 H0 Z" fill="url(#panel-blue)"/>
      </svg>

      <div class="advert-copy">
        <h1>
          <span class="headline-light" style="display:block">PRODUCT</span>
          <span class="headline-bold" style="display:block">TESTING &amp; ANALYSIS</span>
        </h1>
        <div class="divider"></div>
        <ol class="service-list">
          <li class="service-item"><span class="service-number">1</span>Metallurgical Testing</li>
          <li class="service-item"><span class="service-number">2</span>Bearing Pre-load Testing</li>
          <li class="service-item"><span class="service-number">3</span>Bore Measurement</li>
          <li class="service-item"><span class="service-number">4</span>New Product Evaluation</li>
          <li class="service-item"><span class="service-number">5</span>Product Analysis &amp; Report</li>
        </ol>
        <div class="divider divider-lower"></div>
        <p class="contact-phone">0161 555 0192</p>
        <p class="contact-web">www.bolt-remova.co.uk</p>
      </div>

      <p class="company-name">BOLT REMOVA LTD</p>
    </div>
  </div>
</body>
</html>
```